Dental office business cards and stationary
Dr. Mirela Vostok & Dr. Kittipong Wongsalee
Dental office business cards and stationary - Health
Creative Brief
Bright & Fun-filled
Kittipong 'Benny' Wongsalee DDS. Mirela Vostok DMD.
Board Certified Periodontist. Endodontist.
4182 Crestfield Pkwy, Suite 209 Brambleton, VA 22148
T: (703) 481-3907
F: (703) 481-6150
office@glenmarkdentalpair.com
www.glenmarkdentalpair.com
The business card is for two doctors (Dentists) who are marketing their specialty together as a team. They will Market to other doctors only. Not to public. Kittipong 'Benny' Wongsalee, DDS is a 'Board Certified Periodontist'. Mirela Vostok DMD is an 'Endodontist' Card Design Specifics. PLEASE DO NOT DESIGN A LOGO.. The names of the doctor will be the brand. WE would just a color theme which will define the doctors. We are looking at a color theme which will set them apart. Please have cool colors only. Blue, green, peacock blue green, etc. streaks of warm tones may be used. Abstract designs with colors in the back ground is fine. Try and keep a white business card only. With a business card we are looking for three other designs with the similar theme. 1) Letter Head 2) Envelope 3) Referral Pad. (VVIMP) Referral pad design. Size 7 inches x 7 inches. The pad will have front and back side. Front Side Design design elements. 1) The two doctors will have their names and degrees and specialties written. 2) Address and phone numbers. Website. Email 3) A tooth Chart Diagram. The first one on the link. http://www.toothmapzone.co.za/chartguide/dental-chart-tooth-numbering/. 4) Arranged in two columns the procedures that Dr. Kittipong does as follows. 1. Scaling and Root Planing 2. Crown Lengthening 3. Gingivectomy 4. Osseous Surgery for pockets elimination 5. Periodontal Regeneration 6. Soft Tissue Grafting 7. Root Amputation 8. Orthodontic Tooth Exposure 9. Surgical Extractions 10. Bone Grafting/Alveolar Ridge Augmentation 11. Internal and External Sinus Lift 12. Implant Placement 13. TMD Therapy 14. Soft and Hard Tissue Biopsy 5) Arranged in a third column procedures that Dr. Mirela Vostok does. 1. Trauma 2. Cracked Tooth 3. Internal bleaching 4. Apicoectomy 5. Post Space Requested 6. Root Canal Re-treatment 7. Root Canal Therapy 6) Area for Additional comments.
Appointment information. Your next appointment is on___________________________ at _________________ am/pm with Dr._______________________ Please notify us of a cancellation atleast 24hrs in advance to avoid a cancellation fee.
qmelvanor qmelvanor
You can use a slightly different shape, texture of paper, different color gradients for borders..... Since there will be two names(a lot of information) on the card, i would prefer something light as background(as to not overwhelm the card) and play with textures, shapes and borders for the card. Please consider when designing this business card the info above. Please do not include list of procedures the doctors do on the business cards. Thanks.
We did not like the color on 22 and 23. We would like for the card to stand out from a bunch of them.
From the back of the card please remove the names of the doctors and the procedures they do. Please have just the appointment information. Can we have a fancier font please. Also please make a few designs with some different color gradients. The blue and green are too saturated. Thanks.

```html
<!DOCTYPE html>
<html lang="en">
<head>
<meta charset="utf-8">
<title>Wongsalee &amp; Vostok – Business Card</title>
<link href="https://fonts.googleapis.com/css2?family=Cinzel:wght@400;600&family=Cormorant+Garamond:ital,wght@0,400;0,600;1,400&display=swap" rel="stylesheet">
<style>
  :root {
    --page: #e9e6e1;
    --card-white: #fbfbfa;
    --card-dark: #4a4a4b;
    --tab-grey: #8c8c8e;
    --tab-edge: #5e5e60;
    --navy: #25336e;
    --green: #3f7d3a;
    --ink: #3a3a3a;
    --ink-soft: #6b6b6b;
    --on-dark: #f1f1f1;
    --on-dark-soft: #c9c9c9;
  }
  * { box-sizing: border-box; margin: 0; padding: 0; }
  html, body { width: 1200px; height: 1023px; overflow: hidden; }
  body {
    background: var(--page);
    font-family: "Cormorant Garamond", Georgia, serif;
    position: relative;
  }
  .card {
    position: absolute;
    left: 170px;
    width: 860px;
    height: 470px;
    box-shadow: 0 10px 28px rgba(0,0,0,.22);
    overflow: hidden;
  }
  .card--front { top: 32px; background: var(--card-white); }
  .card--back  { top: 530px; background: var(--card-dark); color: var(--on-dark); }

  .tab {
    position: absolute;
    background: var(--tab-grey);
    border: 4px solid var(--tab-edge);
  }
  .card--front .tab--left  { left: -4px; top: 250px; width: 70px; height: 120px; }
  .card--front .tab--right { right: -4px; top: 60px; width: 70px; height: 120px; }
  .card--back .tab--top { left: 40px; top: -4px; width: 120px; height: 66px; }

  .front-names { position: absolute; left: 150px; right: 110px; top: 54px; text-align: center; }
  .doctor-name { font-family: "Cinzel", serif; font-weight: 600; letter-spacing: 1px; }
  .doctor-name--perio { color: var(--navy); font-size: 34px; }
  .doctor-name--endo { color: var(--green); font-size: 30px; margin-top: 10px; }
  .specialty { font-style: italic; font-size: 19px; color: var(--ink-soft); margin-top: 4px; }
  .flourish { display: block; margin: 14px auto 6px; width: 260px; height: 46px; border-radius: 23px;
    background: linear-gradient(90deg, rgba(58,58,58,0), rgba(58,58,58,.35), rgba(58,58,58,0)); }

  .front-contact { position: absolute; left: 110px; right: 60px; bottom: 40px;
    display: flex; justify-content: space-between; align-items: flex-end; font-size: 17px; color: var(--ink); line-height: 1.4; }
  .front-contact .label { color: var(--navy); font-weight: 600; margin-right: 6px; }
  .front-contact .right { text-align: right; }

  .back-header { position: absolute; left: 190px; top: 22px; font-family: "Cinzel", serif; font-size: 20px; letter-spacing: 1px; line-height: 1.35; color: var(--on-dark); }
  .appt-title { position: absolute; left: 190px; top: 104px; font-family: "Cinzel", serif; font-weight: 600; font-size: 26px; letter-spacing: 2px; }
  .appt-fields { position: absolute; left: 80px; right: 70px; top: 160px; }
  .appt-row { display: flex; align-items: flex-end; height: 48px; font-family: "Cinzel", serif; font-size: 19px; letter-spacing: 1px; }
  .appt-row .field-label { width: 110px; }
  .appt-row .field-line { flex: 1; border-bottom: 1.5px solid var(--on-dark-soft); margin-bottom: 6px; }
  .appt-note { position: absolute; left: 80px; right: 70px; bottom: 34px; font-size: 21px; color: var(--on-dark); line-height: 1.3; }
</style>
</head>
<body>

<section class="card card--front" aria-label="Business card front">
  <div class="tab tab--left"></div>
  <div class="tab tab--right"></div>
  <div class="front-names">
    <p class="doctor-name doctor-name--perio">KITTIPONG 'BENNY' WONGSALEE DDS</p>
    <p class="specialty">Board Certified Periodontist</p>
    <div class="flourish" role="img" aria-label="Decorative calligraphic flourish"></div>
    <p class="doctor-name doctor-name--endo">MIRELA VOSTOK DMD</p>
    <p class="specialty">Endodontist</p>
  </div>
  <div class="front-contact">
    <div class="left">
      4182 Crestfield Pkwy, Suite 209<br>
      Brambleton, VA 22148
    </div>
    <div class="right">
      <span class="label">T:</span>(703) 481-3907<br>
      <span class="label">F:</span>(703) 481-6150<br>
      office@glenmarkdentalpair.com<br>
      www.glenmarkdentalpair.com
    </div>
  </div>
</section>

<section class="card card--back" aria-label="Business card back">
  <div class="tab tab--top"></div>
  <div class="back-header">
    KITTIPONG 'BENNY' WONGSALEE DDS<br>
    MIRELA VOSTOK DMD
  </div>
  <h2 class="appt-title">APPOINTMENT</h2>
  <div class="appt-fields">
    <div class="appt-row"><span class="field-label">NAME</span><span class="field-line"></span></div>
    <div class="appt-row"><span class="field-label">DATE</span><span class="field-line"></span></div>
    <div class="appt-row"><span class="field-label">TIME</span><span class="field-line"></span></div>
    <div class="appt-row"><span class="field-label">DOCTOR</span><span class="field-line"></span></div>
  </div>
  <p class="appt-note">Please notify us of a cancellation atleast 24hrs in advance to avoid a cancellation fee.</p>
</section>

</body>
</html>
```